Harbor Nightclub

Nightclub flyer., digital single sided, for KV and PX. I included samples of some previous flyers we've used. Sample Info:
HARBOR
FRIDAYS
FRI MAY 1 2020
DJ VORTAN (club floor)
DJ RUZO & DJ TAV (residents on the lounge floor)
4217 Marlow Avenue Sacramento
www.harborvenuehall.example for list/VIP inquiries

Target Market(s)

Upscale top 40 crowd but want some cool and artsy like the examples included.

Font styles to use
Sans Serif

Requirements
Must have
• Harbor Logo
Nice to have
• Would be nice if the flyer can be incorporated later with DJ photos (sometimes we will add dj photos to pixagram etc). Would like a big city type of feel.
Should not have
• Nothing too sexual.

```html
<!DOCTYPE html>
<html lang="en">
<head>
<meta charset="utf-8">
<title>Harbor Nightclub – Fridays</title>
<link rel="stylesheet" href="https://fonts.googleapis.com/css2?family=Bebas+Neue&family=Oswald:wght@300;400&family=Roboto:wght@300;400;700&display=swap">
<style>
  :root {
    --sky-top: #2c3a9a;
    --sky-violet: #6a3aa6;
    --horizon-magenta: #c23c98;
    --city-dusk: #3a2a6a;
    --city-night: #120d1e;
    --neon-pink: #ff8fd8;
    --neon-glow: rgba(255, 90, 200, 0.75);
    --text-white: #ffffff;
    --text-soft: #e6dcf2;
  }
  * { margin: 0; padding: 0; box-sizing: border-box; }
  html, body { width: 960px; height: 1200px; overflow: hidden; background: var(--city-night); }
  .flyer {
    position: relative;
    width: 960px;
    height: 1200px;
    overflow: hidden;
    font-family: "Roboto", Arial, sans-serif;
    color: var(--text-white);
  }
  .city-backdrop {
    position: absolute;
    inset: 0;
    background:
      radial-gradient(ellipse 70% 18% at 55% 45%, rgba(214, 64, 160, 0.85), transparent 70%),
      linear-gradient(180deg,
        var(--sky-top) 0%,
        var(--sky-violet) 18%,
        #8a3aa8 32%,
        var(--horizon-magenta) 44%,
        var(--city-dusk) 56%,
        #22183e 72%,
        var(--city-night) 100%);
  }
  .venue-address {
    position: absolute;
    top: 38px;
    left: 0;
    width: 960px;
    text-align: center;
    font-weight: 300;
    font-size: 21px;
    letter-spacing: 0.52em;
    color: var(--text-soft);
    white-space: nowrap;
  }
  .neon-frame {
    position: absolute;
    inset: 0;
    width: 960px;
    height: 1200px;
  }
  .brand-kicker {
    position: absolute;
    left: 177px;
    top: 292px;
    font-weight: 400;
    font-size: 30px;
    letter-spacing: 0.02em;
    color: var(--text-white);
  }
  .night-title {
    position: absolute;
    left: 175px;
    top: 326px;
    font-family: "Oswald", "Arial Narrow", sans-serif;
    font-weight: 400;
    font-size: 122px;
    line-height: 1;
    letter-spacing: 0.33em;
    white-space: nowrap;
    color: var(--text-white);
  }
  .event-date {
    position: absolute;
    left: 549px;
    top: 463px;
    font-weight: 700;
    font-size: 35px;
    letter-spacing: 0.12em;
    white-space: nowrap;
    color: var(--text-white);
  }
  .headliner {
    position: absolute;
    left: 0;
    top: 808px;
    width: 960px;
    text-align: center;
    font-family: "Bebas Neue", "Oswald", sans-serif;
    font-weight: 400;
    font-size: 148px;
    line-height: 1;
    white-space: nowrap;
    color: var(--text-white);
    text-shadow: 0 0 14px rgba(255, 150, 220, 0.55);
  }
  .supporting-djs {
    position: absolute;
    left: 0;
    top: 958px;
    width: 960px;
    text-align: center;
    font-family: "Bebas Neue", "Oswald", sans-serif;
    font-weight: 400;
    font-size: 84px;
    line-height: 1;
    white-space: nowrap;
    color: var(--text-white);
    text-shadow: 0 0 12px rgba(255, 150, 220, 0.5);
  }
  .footer {
    position: absolute;
    left: 90px;
    top: 1090px;
    width: 820px;
    height: 60px;
    display: flex;
    align-items: center;
  }
  .brand-mark {
    width: 60px;
    height: 60px;
    border-radius: 50%;
    border: 3px solid var(--text-white);
    margin-right: 17px;
    flex: none;
  }
  .brand-name {
    font-weight: 400;
    font-size: 32px;
    color: var(--text-white);
    margin-right: 56px;
    white-space: nowrap;
  }
  .website {
    font-weight: 300;
    font-size: 21px;
    letter-spacing: 0.26em;
    white-space: nowrap;
    color: var(--text-soft);
  }
</style>
</head>
<body>
  <main class="flyer">
    <div class="city-backdrop" role="img" aria-label="Aerial photograph of a city skyline at dusk in purple and magenta tones"></div>

    <div class="venue-address">4217 MARLOW AVENUE, SACRAMENTO</div>

    <svg class="neon-frame" viewBox="0 0 960 1200" aria-hidden="true">
      <defs>
        <filter id="neon-blur" x="-20%" y="-20%" width="140%" height="140%">
          <feGaussianBlur stdDeviation="9"/>
        </filter>
      </defs>
      <polygon points="113,185 830,267 907,555 72,647" fill="none" stroke="var(--neon-glow)" stroke-width="14" filter="url(#neon-blur)"/>
      <polygon points="113,185 830,267 907,555 72,647" fill="none" stroke="var(--neon-pink)" stroke-width="2.5"/>
    </svg>

    <div class="brand-kicker">HARBOR</div>
    <h1 class="night-title">FRIDAYS</h1>
    <div class="event-date">MAY 1 2020</div>

    <h2 class="headliner">DJ VORTAN</h2>
    <h3 class="supporting-djs">DJ RUZO &amp; DJ TAV</h3>

    <footer class="footer">
      <span class="brand-mark" aria-hidden="true"></span>
      <span class="brand-name">HARBOR</span>
      <span class="website">WWW.HARBORVENUEHALL.EXAMPLE</span>
    </footer>
  </main>
</body>
</html>
```